Marketing Expert Needs a Book Cover Design to Inspire Audiences

Need a book cover design for my first book!
The book is a ‘How To’ serious non fiction book. It has insights for marketers on how to transform their marketing to help their organizations accelerate sales and drive growth. This is not a high level theoretical book about brand building. Instead this includes strategic frameworks, and tried and tested ideas and tactics which marketers (or aspiring marketers) can use to be successful in their jobs. The premise of this book is that it’s no longer enough for marketers to focus on brand recognition. We need to help the business to create demand and make it easier for our sales colleagues to close deals.
The aim is to inspire readers with insights so that they think differently about themselves and their marketing. The aim is to compel them to take start new conversations to accelerate sales, using the tools, concepts and case studies outlined in the book.
The Title: The Growth Signal
Subtitle: Steps to Win Buyers by Storytelling, Curiosity and Trusted Voices.
The cover must have a compelling visual which communicates this idea-
The Growth Signal Inspires You to Think Different so That You Scale/Overcome the Limits you might have placed on yourself or your business.
I like a simple and clean look. I'm attaching some samples which I like. Looking to achieve the same look for my book cover.
Update- I need the cover for an ebook only. Since the cover will be displayed as a thumbnail in Verbolt and other online shopping sites, it should be without any clutter with good contrast between images and text. This will help with visibility.
Updates
Key Art Style designs will also be welcome. Added Saturday, September 24, 2016
Reason: I'm hoping that atleast some more top 20 designers will respond.
Target Market(s)
Target market is CMOs, Marketing Managers, Business Leaders, MBA students- anyone who is looking to reshape and rejig their marketing skills and teams.
Industry/Entity Type
Marketing
Requirements
Must have
- A compelling visual is a must have.
- It shouldn't have only text.
Nice to have
- Please refer the cover samples I sent.
- Key Art designs will also be welcome.
Should not have
- Clutter.
- I like simplicity.

```html
<!DOCTYPE html>
<html lang="en">
<head>
<meta charset="utf-8">
<title>The Growth Signal — Book Cover</title>
<link rel="stylesheet" href="https://fonts.googleapis.com/css2?family=Anton&family=Open+Sans:wght@400;600&display=swap">
<style>
  :root {
    --stage: #e8e8e8;
    --blue-deep: #1f5fb8;
    --blue-mid: #1f7fd6;
    --blue-light: #39a7e4;
    --title-white: #f2f4f6;
    --title-yellow: #f2e11a;
    --band-yellow: #f0e41c;
    --ink: #111111;
    --silhouette: #1a2a44;
    --red: #e2234f;
    --orange: #f07a1e;
    --green: #1e9a43;
    --teal: #2aa59a;
  }
  * { margin: 0; padding: 0; box-sizing: border-box; }
  html, body {
    width: 1200px; height: 1200px; overflow: hidden;
    background: var(--stage);
  }
  .cover {
    position: absolute;
    left: 190px; top: 50px;
    width: 820px; height: 1100px;
    overflow: hidden;
    background: linear-gradient(200deg, var(--blue-light) 0%, var(--blue-mid) 35%, var(--blue-deep) 100%);
    box-shadow: 0 20px 50px rgba(0,0,0,0.25);
  }
  .team-figures {
    position: absolute;
    left: 300px; top: 95px;
    width: 170px; height: 170px;
    background: linear-gradient(180deg, rgba(26,42,68,0.55), rgba(26,42,68,0.35));
    border-radius: 8px;
  }
  .title {
    position: absolute;
    left: 60px; top: 170px;
    font-family: "Anton", "Oswald", sans-serif;
    font-weight: 400;
    text-transform: uppercase;
    line-height: 0.95;
  }
  .title-line {
    display: block;
  }
  .title-the {
    color: var(--title-white);
    font-size: 110px;
    letter-spacing: 2px;
  }
  .title-growth {
    color: var(--title-white);
    font-size: 120px;
    letter-spacing: 2px;
  }
  .title-signal {
    color: var(--title-yellow);
    font-size: 230px;
    letter-spacing: 6px;
  }
  .subtitle {
    position: absolute;
    left: 64px; top: 625px;
    font-family: "Open Sans", sans-serif;
  }
  .subtitle-top {
    display: block;
    color: var(--title-white);
    font-size: 25px;
    font-weight: 400;
  }
  .subtitle-bottom {
    display: block;
    color: var(--title-yellow);
    font-size: 31px;
    font-weight: 600;
    margin-top: 2px;
  }
  .growth-arrows {
    position: absolute;
    left: 0; top: 725px;
    width: 820px; height: 375px;
    background: linear-gradient(90deg, var(--blue-light) 0%, var(--orange) 22%, var(--red) 42%, var(--title-yellow) 55%, var(--orange) 70%, var(--green) 85%, var(--teal) 100%);
    clip-path: polygon(0 100%, 0 45%, 12% 30%, 22% 10%, 34% 22%, 45% 0, 56% 18%, 66% 4%, 78% 20%, 90% 0, 100% 12%, 100% 100%);
  }
  .author-band {
    position: absolute;
    left: 0; top: 960px;
    width: 820px; height: 66px;
    background: var(--band-yellow);
    opacity: 0.94;
    display: flex; align-items: center; justify-content: center;
  }
  .author-name {
    font-family: "Open Sans", sans-serif;
    font-size: 30px;
    letter-spacing: 9px;
    color: var(--ink);
    text-transform: uppercase;
  }
</style>
</head>
<body>
  <main class="cover">
    <div class="team-figures" role="img" aria-label="Silhouettes of three business people standing together"></div>
    <h1 class="title">
      <span class="title-line title-the">The</span>
      <span class="title-line title-growth">Growth</span>
      <span class="title-line title-signal">Signal</span>
    </h1>
    <p class="subtitle">
      <span class="subtitle-top">Steps to Win Buyers by Storytelling,</span>
      <span class="subtitle-bottom">Curiosity and Trusted Voices.</span>
    </p>
    <div class="growth-arrows" role="img" aria-label="Colourful pixelated arrows rising upward like a growth chart"></div>
    <div class="author-band">
      <span class="author-name">Author's Name</span>
    </div>
  </main>
</body>
</html>
```